International ecosystem needs business model upgrade

We need an upgrade from our business model. We already have a sketch that needs be 'upgraded'. Ugraded means better colors, smoother lines. It needs to be more attractive. We would like to see the use of colour blue and white aspects. It must remain simple.

If you want extra information about the model. Feel free to contact me. The words in the model are written in Dutch. See below descriptions for more specific information about this project.

Summit Circle is a cross sectoral network of more than 400 CEO’s/General Managers within The Netherlands. Members are all responsible for large or medium sized organizations. The goal of the network is to enable cross sectoral learning as well as establish collaborations and business deals between its members. In order to realize this the business matching team of the Summit Circle organization proactively initiates value adding introductions between its members. Furthermore Summit Circle organizes a wide range of masterclasses, round tables, dinners and company visits.

Target Market(s)

CEO, Directors

Industry/Entity Type

Business

Font styles to use
Sans Serif

Colors
85cae6
33a6d7
ffffff
0355a3
000000

Requirements
Must have
• The model has to be understandable (not to complex).
• The file attatched should be used as a basis.
Nice to have
• A model without text would be prefferable. We can add texts later.
Should not have
• Extra text

```html
<!DOCTYPE html>
<html lang="nl">
<head>
<meta charset="utf-8">
<title>Leiderschapsmodel – Leider, Organisatie, Omgeving</title>
<link href="https://fonts.googleapis.com/css2?family=Source+Sans+3:wght@400;600;700&display=swap" rel="stylesheet">
<style>
  :root {
    --white: #ffffff;
    --sky-light: #c9e7f5;
    --sky: #85cae6;
    --azure: #33a6d7;
    --periwinkle: #8aa6dc;
    --deep-blue: #0a6fbf;
    --navy: #0355a3;
    --amber: #fbb040;
    --label-blue: #33a6d7;
  }
  html, body {
    margin: 0;
    padding: 0;
    width: 1200px;
    height: 906px;
    overflow: hidden;
    background: var(--white);
  }
  .model {
    display: block;
    width: 1200px;
    height: 906px;
    font-family: "Source Sans 3", "Myriad Pro", sans-serif;
  }
  .sphere-label {
    fill: var(--white);
    font-weight: 600;
    font-size: 24px;
    letter-spacing: 0.2px;
  }
  .identity-label {
    fill: var(--white);
    font-size: 16.5px;
  }
  .value-bar { fill: var(--white); }
  .value-label {
    fill: var(--label-blue);
    font-size: 16px;
  }
  .creative-label {
    fill: var(--white);
    font-weight: 600;
    font-size: 20px;
    letter-spacing: 0.4px;
  }
  .arrow { fill: var(--amber); }
</style>
</head>
<body>
<svg class="model" viewBox="0 0 1200 906" xmlns="http://www.w3.org/2000/svg" role="img" aria-label="Model met drie sferen: leider, organisatie en omgeving, doorsneden door een pijl">
  <defs>
    <linearGradient id="grad-omgeving" x1="560" y1="0" x2="865" y2="0" gradientUnits="userSpaceOnUse">
      <stop offset="0" stop-color="var(--periwinkle)"/>
      <stop offset="1" stop-color="var(--deep-blue)"/>
    </linearGradient>
    <linearGradient id="grad-organisatie" x1="240" y1="0" x2="665" y2="0" gradientUnits="userSpaceOnUse">
      <stop offset="0" stop-color="#c3e2f3"/>
      <stop offset="0.45" stop-color="#8fbfe6"/>
      <stop offset="1" stop-color="var(--azure)"/>
    </linearGradient>
    <linearGradient id="grad-leider" x1="218" y1="0" x2="476" y2="0" gradientUnits="userSpaceOnUse">
      <stop offset="0" stop-color="var(--sky-light)"/>
      <stop offset="1" stop-color="var(--sky)"/>
    </linearGradient>
  </defs>

  <g class="spheres">
    <path class="sphere sphere--omgeving" d="M232,502 L728,107 A644,644 0 0 1 797,789 Z" fill="url(#grad-omgeving)"/>
    <path class="sphere sphere--organisatie" d="M230,502 L548,208 A445,445 0 0 1 604,732 Z" fill="url(#grad-organisatie)" opacity="0.92"/>
    <path class="sphere sphere--leider" d="M218,502 L395,312 A259,259 0 0 1 428,652 Z" fill="url(#grad-leider)" opacity="0.9"/>
  </g>

  <text class="sphere-label" x="632" y="249">OMGEVING</text>
  <text class="sphere-label" x="455" y="355">ORGANISATIE</text>
  <text class="sphere-label" x="335" y="420">LEIDER</text>

  <g class="growth-arrow">
    <path class="arrow" d="M320,442 H745 V418 L855,493 L745,568 V548 H320 Z"/>

    <text class="identity-label" transform="translate(363,458) rotate(90)">werkelijke</text>
    <text class="identity-label" transform="translate(345,458) rotate(90)">identiteit</text>

    <rect class="value-bar" x="397" y="455" width="266" height="17"/>
    <text class="value-label" x="402" y="469">Spiritueel</text>
    <rect class="value-bar" x="397" y="475" width="281" height="17"/>
    <text class="value-label" x="425" y="489">Duurzaam</text>
    <rect class="value-bar" x="397" y="496" width="281" height="17"/>
    <text class="value-label" x="425" y="510">Technologisch</text>
    <rect class="value-bar" x="397" y="516" width="266" height="17"/>
    <text class="value-label" x="402" y="530">Economisch</text>

    <text class="creative-label" transform="translate(716,451) rotate(90)">CREATIVE</text>
  </g>
</svg>
</body>
</html>
```